lumVex mobile app needs Banner Ad

"See who is around"
I'm looking for a Banner Ad for mobile application. The application is available at Fernway Shelf and Quillon Depot. Details are on the website:
http://lumvex.example

Video is here:
http://vidnook.example/Qr8Tz2Wm4Lp

I'd either use the mobile app button or the globe from logo in Banner Ad.

Sizes needed are:
320x50
640x100

```html
<!DOCTYPE html>
<html lang="en">
<head>
<meta charset="utf-8">
<title>lumVex banner ads</title>
<link rel="stylesheet" href="https://fonts.googleapis.com/css2?family=Comfortaa:wght@400&family=Ubuntu:wght@700&display=swap">
<style>
  :root {
    --stage: #6b4a2e;
    --accent-orange: #f07a14;
    --panel-white: #ffffff;
    --panel-shade: #e9ebee;
    --brand-ink: #2a2a2a;
    --tagline-blue: #1a86f0;
    --globe-blue: #1f63c8;
    --globe-light: #4aa3f0;
    --device-dark: #2b2d31;
    --device-screen: #8fb7cf;
  }
  * { margin: 0; padding: 0; box-sizing: border-box; }
  html, body {
    width: 1200px; height: 420px; overflow: hidden;
    background: var(--stage);
  }
  .canvas { position: relative; width: 1200px; height: 420px; }

  .banner {
    position: absolute;
    width: 1000px; height: 156px;
    background: var(--accent-orange);
    box-shadow: 0 6px 14px rgba(0,0,0,.35);
  }
  .banner--large { left: 102px; top: 75px; }
  .banner--small { left: 352px; top: 266px; transform: scale(.496); transform-origin: top left; }

  .banner__panel {
    position: absolute; left: 8px; right: 8px; top: 0; bottom: 0;
    background: linear-gradient(180deg, var(--panel-white) 0%, var(--panel-shade) 100%);
    border-radius: 60px 60px 60px 60px / 78px 78px 78px 78px;
    overflow: hidden;
  }

  .banner__mark {
    position: absolute; left: 62px; top: 28px;
    width: 104px; height: 104px; border-radius: 50%;
    background: radial-gradient(circle at 35% 30%, var(--globe-light), var(--globe-blue) 70%);
  }

  .banner__brand {
    position: absolute; left: 0; right: 0; top: 10px;
    text-align: center;
    font-family: "Comfortaa", sans-serif; font-weight: 400;
    font-size: 60px; line-height: 1; color: var(--brand-ink);
  }

  .banner__tagline {
    position: absolute; left: 0; right: 0; top: 92px;
    text-align: center;
    font-family: "Ubuntu", sans-serif; font-weight: 700;
    font-size: 38px; line-height: 1; color: var(--tagline-blue);
    text-shadow: 0 0 6px rgba(255,255,255,.9);
  }

  .banner__device {
    position: absolute; right: 0; top: 6px;
    width: 170px; height: 150px;
    border-radius: 28px 0 0 0;
    background: linear-gradient(150deg, var(--device-dark) 0%, var(--device-dark) 25%, var(--device-screen) 26%, #c9a675 70%, var(--device-dark) 71%);
  }
</style>
</head>
<body>
<main class="canvas">
  <section class="banner banner--large" aria-label="640 by 100 banner">
    <div class="banner__panel">
      <span class="banner__mark" aria-hidden="true"></span>
      <h1 class="banner__brand">lumVex</h1>
      <p class="banner__tagline">See who is around</p>
      <div class="banner__device" role="img" aria-label="Smartphone showing the app's map screen"></div>
    </div>
  </section>

  <section class="banner banner--small" aria-label="320 by 50 banner">
    <div class="banner__panel">
      <span class="banner__mark" aria-hidden="true"></span>
      <h2 class="banner__brand">lumVex</h2>
      <p class="banner__tagline">See who is around</p>
      <div class="banner__device" role="img" aria-label="Smartphone showing the app's map screen"></div>
    </div>
  </section>
</main>
</body>
</html>
```